New Alcoholic Spiked Seltzer Line

We need a can design for a line of low calorie alcoholic seltzer. This product is a sparkling water and vodka drink with no sugar added in a slim 12 oz can.

This is a lighter, healthier, alternative to the sugary ready-to-drinks on the market. The product contains only 3 ingredients: Vodka, Water and Natural Flavors. It has only 100 calories but still has 5% alcohol, so you don't need to sacrifice alcohol to cut calories.

This product also does not contain any preservatives.

We want this design to communicate the following objectives to the consumer and in this order:

1. Appetizing product
2.Low calorie
3.Communicate the type of beverage (Spiked Seltzer)

The brand name of the product is VELKA.

The flavor of the product needed to be used for the design is Mango-Orange.

Comparable products are:

www.brisavelfizz.example/
https://www.tarnowbubble.example
https://quellrind.example/

The designs should not infringe or copy the creative directions of the products mentionned above. They are only given so that you can better understand the type of product we are developing.

Target Market(s)

Young Professional women between the ages of 25 and 44

Industry/Entity Type

Product

Colors

Designer to choose colors to be used in the design.

Requirements
Must have
• Design extendibility, meaning it can be adapted for other flavors.
• This is a new category in the market we are targeting, so consumers must easily be able to identify what type of product this is.

```html
<!DOCTYPE html>
<html lang="en">
<head>
<meta charset="utf-8">
<title>VELKA Spiked Seltzer – Mango &amp; Orange can label</title>
<link rel="stylesheet" href="https://fonts.googleapis.com/css2?family=Marcellus&family=Oswald:wght@300&family=Roboto+Condensed:wght@400&family=Damion&display=swap">
<style>
  :root {
    --backdrop: #e8eaee;
    --label-white: #ffffff;
    --band-orange: #f4a93a;
    --script-orange: #f0a526;
    --ink: #2a2a2a;
    --pattern-grey: #efefef;
    --band-text: #fff6e6;
    --fruit-red: #d8383a;
    --fruit-yellow: #f2b52a;
  }
  * { margin: 0; padding: 0; box-sizing: border-box; }
  html, body {
    width: 1200px; height: 1200px; overflow: hidden;
    background: var(--backdrop);
  }
  .can-label {
    position: absolute;
    left: 380px; top: 55px;
    width: 440px; height: 1090px;
    background: var(--label-white);
    overflow: hidden;
  }
  .band {
    position: absolute; left: 0; width: 100%;
    background: var(--band-orange);
    color: var(--band-text);
    font-family: "Roboto Condensed", "Arial Narrow", sans-serif;
    text-transform: uppercase;
    text-align: center;
    white-space: nowrap;
    display: flex; align-items: center; justify-content: center;
  }
  .band--top { top: 0; height: 45px; font-size: 16px; letter-spacing: -0.3px; }
  .band--bottom { bottom: 0; height: 62px; font-size: 20px; }
  .brand-name {
    position: absolute; top: 100px; left: 0; width: 100%;
    text-align: center;
    font-family: "Marcellus", serif;
    font-size: 122px; line-height: 1;
    color: var(--ink);
    letter-spacing: 2px;
    white-space: nowrap;
  }
  .category {
    position: absolute; top: 262px; left: 0; width: 100%;
    text-align: center;
    font-family: "Oswald", sans-serif; font-weight: 300;
    font-size: 34px; letter-spacing: 4px;
    color: var(--ink);
    white-space: nowrap;
  }
  .pattern-field {
    position: absolute; left: 0; top: 697px; width: 100%; height: 340px;
    background: linear-gradient(180deg, var(--label-white) 0%, var(--pattern-grey) 40%, var(--pattern-grey) 100%);
  }
  .fruit-photo {
    position: absolute; left: 14px; top: 360px; width: 414px; height: 365px;
    border-radius: 46% 54% 48% 52% / 50% 50% 50% 50%;
    background: radial-gradient(circle at 45% 35%, var(--fruit-red) 0%, #e8813a 38%, var(--fruit-yellow) 70%, rgba(255,255,255,0) 74%);
  }
  .flavor-intro {
    position: absolute; top: 765px; left: 0; width: 100%;
    text-align: center;
    font-family: "Roboto Condensed", sans-serif;
    font-size: 25px; line-height: 1.2; color: var(--ink);
    white-space: nowrap;
  }
  .flavor-name {
    position: absolute; top: 800px; left: 0; width: 100%;
    text-align: center;
    font-family: "Damion", cursive;
    font-size: 56px; line-height: 1.2;
    color: var(--script-orange);
    white-space: nowrap;
  }
  .claim-tag {
    position: absolute; top: 912px; left: 136px; width: 168px; height: 39px;
    background: var(--band-orange);
    color: var(--label-white);
    font-family: "Roboto Condensed", sans-serif;
    font-size: 22px;
    white-space: nowrap;
    display: flex; align-items: center; justify-content: center;
  }
  .abv {
    position: absolute; top: 985px; left: 0; width: 100%;
    text-align: center;
    font-family: "Roboto Condensed", sans-serif;
    font-size: 23px; line-height: 1.2; color: var(--ink);
    white-space: nowrap;
  }
</style>
</head>
<body>
  <main class="can-label">
    <div class="band band--top">This product does not contain any preservatives.</div>
    <h1 class="brand-name">VELKA</h1>
    <p class="category">SPIKED SELTZER</p>
    <div class="pattern-field" role="img" aria-label="Faint grey triangle pattern"></div>
    <div class="fruit-photo" role="img" aria-label="Photo of a whole mango with leaf, mango slices and a halved orange"></div>
    <p class="flavor-intro">With a hint of</p>
    <p class="flavor-name">Mango &amp; Orange</p>
    <div class="claim-tag">LOW CALORIE</div>
    <p class="abv">5% ALC./VOL.</p>
    <div class="band band--bottom">Vodka, water and natural flavors.</div>
  </main>
</body>
</html>
```